elearning course template

Our company has a variety of elearning courses. We are currently redesigning the courses and are looking for a new layout for the online learning courses. The layout should be 800x600 and it needs to incorporate the following elements:
1. Course Name
2. Chapter Name
3. Page name
4. Our company logo (see attached file)
5. Navigation bar that includes:
- Next / back buttons
- Page count
- Audio control bar (see attached file)
- Menu items that include: "Menu, Transcript, Resources"
9. Exit button (may be included on the navigation bar if appropriate)
10. Content area must be 775 wide x 442 high

We would like to see designs that use our company colors, blue (RGB 0,69,144) and orange (RGB 222, 111, 51) and dark gray. We're looking for a solution that is clean, crisp and very user friendly. We'd also like to see a little dimension in the layout, we feel that our current layout is very "flat".

You can find out more about our company at www.fenlark-vro.com.

Industry/Entity Type

Graphic Design

```html
<!DOCTYPE html>
<html lang="en">
<head>
<meta charset="utf-8">
<title>eLearning Course Player</title>
<link href="https://fonts.googleapis.com/css2?family=Questrial&display=swap" rel="stylesheet">
<style>
  :root {
    --blue: #004590;
    --blue-deep: #0f3f7a;
    --orange: #de6f33;
    --orange-dark: #c75a22;
    --frame: #3a3a3a;
    --bar-grey: #d4d4d4;
    --track-grey: #9a9a9a;
    --white: #ffffff;
    --text-dark: #4a4a4a;
  }
  * { box-sizing: border-box; margin: 0; padding: 0; }
  html, body { width: 1200px; height: 900px; overflow: hidden; background: var(--frame); }
  body { font-family: "Questrial", "Century Gothic", sans-serif; }

  .player { position: absolute; left: 4px; top: 4px; width: 1192px; height: 892px; background: var(--white); overflow: hidden; }

  .header { position: absolute; left: 0; top: 0; width: 100%; height: 102px; background: linear-gradient(to bottom, #13467f, var(--blue-deep)); }
  .title-bar { position: absolute; left: 0; top: 102px; width: 100%; height: 34px; background: linear-gradient(to bottom, #e77a3e, var(--orange)); }
  .title-bar .crumb { position: absolute; left: 103px; top: 7px; color: var(--white); font-size: 18px; }

  .page-curl { position: absolute; left: 0; top: 0; width: 220px; height: 160px; }
  .brand { position: absolute; left: 16px; top: 22px; display: flex; align-items: center; gap: 6px; }
  .brand .mark { width: 14px; height: 14px; border-radius: 50%; background: var(--orange); }
  .brand .name { font-size: 26px; color: var(--blue); font-weight: 400; }

  .exit { position: absolute; left: 1139px; top: 23px; width: 39px; height: 34px; background: linear-gradient(#ffffff, #e6e6e6); border: 1px solid #b8b8b8; border-radius: 4px; }
  .exit svg { position: absolute; left: 11px; top: 9px; }

  .content { position: absolute; left: 0; top: 136px; width: 100%; height: 680px; background: var(--white); }

  .timeline { position: absolute; left: 0; top: 818px; width: 100%; height: 8px; background: var(--track-grey); border-top: 1px solid #7e7e7e; }
  .timeline .played { position: absolute; left: 0; top: 0; height: 100%; width: 593px; background: var(--orange); }
  .timeline .knob { position: absolute; left: 582px; top: -7px; width: 22px; height: 22px; border-radius: 50%; background: radial-gradient(circle, var(--orange) 0 3px, #f4f4f4 4px); border: 1px solid #b0b0b0; }
  .time-tip { position: absolute; left: 89px; top: 785px; width: 57px; height: 26px; background: var(--white); border: 1px solid #c4c4c4; border-radius: 3px; font-size: 17px; color: var(--text-dark); text-align: center; line-height: 24px; }

  .controls { position: absolute; left: 0; top: 826px; width: 100%; height: 66px; background: linear-gradient(to bottom, #dcdcdc, #cacaca); }
  .volume-icon { position: absolute; left: 22px; top: 19px; }
  .volume-track { position: absolute; left: 59px; top: 33px; width: 240px; height: 5px; background: #b9b9b9; border-radius: 3px; }
  .volume-track .level { position: absolute; left: 0; top: 0; width: 155px; height: 100%; background: var(--orange); border-radius: 3px; }
  .volume-track .knob { position: absolute; left: 50px; top: -6px; width: 17px; height: 17px; border-radius: 50%; background: radial-gradient(circle, #8a8a8a 0 3px, #f4f4f4 4px); border: 1px solid #aaa; }

  .divider { position: absolute; top: 11px; width: 2px; height: 46px; background: #8c8c8c; border-right: 1px solid #f0f0f0; }

  .nav-btn { position: absolute; top: 8px; width: 50px; height: 50px; border-radius: 50%; }
  .nav-btn svg { position: absolute; left: 18px; top: 17px; }
  .nav-back { left: 508px; background: linear-gradient(#ffffff, #e2e2e2); border: 1px solid #b0b0b0; }
  .nav-next { left: 655px; background: linear-gradient(#e9854c, var(--orange-dark)); border: 1px solid #b05020; }
  .page-count { position: absolute; left: 570px; top: 21px; width: 75px; text-align: center; font-size: 20px; color: var(--text-dark); }
  .page-count .total { color: #888; }

  .menu-btn { position: absolute; top: 5px; width: 111px; height: 54px; border-radius: 3px; font-size: 18px; text-align: center; line-height: 52px; box-shadow: 0 2px 2px rgba(0,0,0,0.25); }
  .menu-btn.primary { background: linear-gradient(#e77f45, var(--orange-dark)); color: var(--white); border: 1px solid #b3531f; }
  .menu-btn.active { background: linear-gradient(#ffffff, #ececec); color: var(--orange); border: 1px solid #bdbdbd; }
</style>
</head>
<body>
<div class="player">
  <header class="header"></header>
  <div class="title-bar"><span class="crumb">Course Name- Chapter Name - Page name</span></div>

  <svg class="page-curl" viewBox="0 0 220 160" aria-hidden="true">
    <defs>
      <linearGradient id="curlShade" x1="0" y1="0" x2="1" y2="1">
        <stop offset="0" stop-color="#ffffff"/>
        <stop offset="0.65" stop-color="#f2f2f2"/>
        <stop offset="1" stop-color="#bfbfbf"/>
      </linearGradient>
      <filter id="curlShadow" x="-20%" y="-20%" width="140%" height="140%">
        <feDropShadow dx="3" dy="4" stdDeviation="4" flood-opacity="0.35"/>
      </filter>
    </defs>
    <path d="M0 0 H208 Q160 55 120 95 Q70 125 30 150 Q10 140 0 142 Z" fill="url(#curlShade)" filter="url(#curlShadow)"/>
    <path d="M208 0 Q180 60 120 95 Q150 55 170 20 Z" fill="#d9d9d9"/>
  </svg>
  <div class="brand"><span class="mark"></span><span class="name">Fenlark</span></div>

  <div class="exit" aria-label="Exit">
    <svg width="16" height="16" viewBox="0 0 16 16"><path d="M2 2 L14 14 M14 2 L2 14" stroke="#de6f33" stroke-width="3" stroke-linecap="round"/></svg>
  </div>

  <main class="content"></main>

  <div class="time-tip">0:20</div>
  <div class="timeline"><div class="played"></div><div class="knob"></div></div>

  <nav class="controls">
    <svg class="volume-icon" width="34" height="30" viewBox="0 0 34 30" aria-label="Volume">
      <path d="M2 10 H9 L18 2 V28 L9 20 H2 Z" fill="#de6f33"/>
      <path d="M23 9 Q27 15 23 21" stroke="#de6f33" stroke-width="2.5" fill="none" stroke-linecap="round"/>
    </svg>
    <div class="volume-track"><div class="level"></div><div class="knob"></div></div>

    <div class="divider" style="left:468px"></div>
    <div class="nav-btn nav-back" aria-label="Back">
      <svg width="14" height="16" viewBox="0 0 14 16"><path d="M12 1 L2 8 L12 15 Z" fill="#de6f33"/></svg>
    </div>
    <div class="page-count">2 / <span class="total">10</span></div>
    <div class="nav-btn nav-next" aria-label="Next">
      <svg width="14" height="16" viewBox="0 0 14 16"><path d="M3 1 L13 8 L3 15 Z" fill="#ffffff"/></svg>
    </div>
    <div class="divider" style="left:745px"></div>

    <div class="menu-btn primary" style="left:783px">Menu</div>
    <div class="menu-btn active" style="left:921px">Transcript</div>
    <div class="menu-btn primary" style="left:1059px">Resources</div>
  </nav>
</div>
</body>
</html>
```